I need a business card to give to prospective clients. I am a freelance photographer who photographs most things (except weddings and social stuff) including nature, wildlife and interiors.
I want to look modern and stylish.
I am including a photograph although I am by no means certain that it should be used - what do you think?
More of my images can be seen and downloaded at my Lensora page - just search for Marla Vintree
Target Market(s)
Home owners selling or letting properties, private individuals wanting to buy prints
Industry/Entity Type
Business
Contact Information for Business Card
Marla Vintree Photography
Marla
Fenwick Lodge, Copper Mill Road, Ashbrook, Harrowmere, QX4 7NB
Tel: +44 7700 418263. Email: marla@marlavintree.co.uk

```html
<!DOCTYPE html>
<html lang="en">
<head>
<meta charset="utf-8">
<title>Marla Vintree Photography – Business Card</title>
<link rel="stylesheet" href="https://fonts.googleapis.com/css2?family=Tinos:wght@400;700&family=Playfair+Display:wght@700&display=swap">
<style>
  :root {
    --page-bg: #e9e6e0;
    --back-dark: #2e2e2e;
    --back-mid: #555555;
    --back-light: #6e6e6e;
    --front-dark: #4a4a4a;
    --front-mid: #8c8c8c;
    --front-light: #d4d4d4;
    --title-grey: #a3a3a3;
    --text-white: #ffffff;
    --bracket: #e6e6e6;
    --card-shadow: rgba(0, 0, 0, 0.35);
  }
  * { box-sizing: border-box; margin: 0; padding: 0; }
  html, body { width: 1200px; height: 750px; overflow: hidden; }
  body {
    background: var(--page-bg);
    display: flex;
    align-items: center;
    justify-content: center;
    gap: 40px;
  }
  .card {
    position: relative;
    width: 560px;
    height: 318px;
    overflow: hidden;
    box-shadow: 0 6px 18px var(--card-shadow);
  }
  .card-photo {
    position: absolute;
    inset: 0;
  }
  .card--back .card-photo {
    background:
      radial-gradient(ellipse 45% 60% at 62% 48%, var(--back-light), transparent 70%),
      linear-gradient(180deg, var(--back-mid) 0%, var(--back-dark) 55%, var(--back-mid) 100%);
  }
  .card--front .card-photo {
    background:
      radial-gradient(ellipse 40% 55% at 58% 52%, var(--front-dark), transparent 75%),
      linear-gradient(90deg, var(--front-mid) 0%, var(--front-dark) 30%, var(--front-mid) 55%, var(--front-dark) 85%, var(--front-mid) 100%),
      linear-gradient(180deg, transparent 70%, var(--front-light) 100%);
    background-blend-mode: normal, normal, screen;
  }
  .corner {
    position: absolute;
    width: 22px;
    height: 22px;
    border-color: var(--bracket);
    border-style: solid;
    border-width: 0;
  }
  .corner--tl { border-top-width: 3px; border-left-width: 3px; }
  .corner--tr { border-top-width: 3px; border-right-width: 3px; }
  .corner--bl { border-bottom-width: 3px; border-left-width: 3px; }
  .corner--br { border-bottom-width: 3px; border-right-width: 3px; }

  .card--back .corner--tl { top: 52px; left: 28px; }
  .card--back .corner--tr { top: 20px; right: 28px; }
  .card--back .corner--bl { bottom: 22px; left: 58px; }

  .card--front .corner--tl { top: 24px; left: 24px; }
  .card--front .corner--tr { top: 122px; right: 24px; }
  .card--front .corner--bl { bottom: 58px; left: 24px; }
  .card--front .corner--br { bottom: 22px; right: 52px; }

  .contact {
    position: absolute;
    left: 176px;
    top: 62px;
    font-family: "Tinos", "Times New Roman", serif;
    color: var(--text-white);
  }
  .contact-title {
    font-size: 29px;
    font-weight: 400;
    color: var(--title-grey);
    margin-left: 10px;
    margin-bottom: 14px;
    white-space: nowrap;
  }
  .contact-line {
    font-size: 17px;
    line-height: 1.4;
  }
  .contact-address {
    font-style: normal;
    font-size: 12.5px;
    line-height: 1.5;
    margin-top: 16px;
  }
  .brand {
    position: absolute;
    top: 138px;
    left: 0;
    right: 0;
    text-align: center;
    font-family: "Playfair Display", "Times New Roman", serif;
    font-weight: 700;
    color: var(--text-white);
    text-transform: uppercase;
  }
  .brand-name {
    font-size: 38px;
    letter-spacing: 1px;
    line-height: 1;
  }
  .brand-tag {
    font-size: 22px;
    letter-spacing: 2px;
    margin-top: 4px;
  }
</style>
</head>
<body>
  <section class="card card--back">
    <div class="card-photo" role="img" aria-label="Dark monochrome close-up photograph of an elephant's legs and curled trunk in grass"></div>
    <span class="corner corner--tl"></span>
    <span class="corner corner--tr"></span>
    <span class="corner corner--bl"></span>
    <div class="contact">
      <h2 class="contact-title">Marla Vintree Photography</h2>
      <p class="contact-line">Tel: +44 7700 418263</p>
      <p class="contact-line">Email: marla@marlavintree.co.uk</p>
      <address class="contact-address">
        Marla Vintree Photography Fenwick Lodge,<br>
        Copper Mill Road,<br>
        Ashbrook,<br>
        Harrowmere,<br>
        QX4 7NB
      </address>
    </div>
  </section>

  <section class="card card--front">
    <div class="card-photo" role="img" aria-label="Black and white photograph of an elephant's legs with its trunk curled over the grass"></div>
    <span class="corner corner--tl"></span>
    <span class="corner corner--tr"></span>
    <span class="corner corner--bl"></span>
    <span class="corner corner--br"></span>
    <div class="brand">
      <h1 class="brand-name">Marla Vintree</h1>
      <p class="brand-tag">Photography</p>
    </div>
  </section>
</body>
</html>
```